Alcohol Marketing website

Home page and information page design, details as follows

CLIENT PURPOSE
Increase online visibility and create good contacts to increase business.

SERVICES
Drinks Marketing Consultancy
Brand Representation
Spirit Brand Sales & Marketing
Brand Development
Brand Distribution
Brand Launch & Introductions

COMPETITION
merrycasks.co.uk -
talvoranbrands.co.uk -

WEBSITE(S) CLIENT LIKES
Small competitors I admire:
http://www.merrycasks.co.uk/main.htm
http://www.talvoranbrands.com
http://www.vaultpicks.co.uk/spiritsliqueursbybrand.php
http://www.quellomarks.com/page1.html
http://www.zirnopaxtra.co.uk/index.asp

Nice page layout:
http://www.kvworks.com/
http://www.dmhallies.com/
http://www.pelvik.com/index.cfm?do=pelvik.home

WEBSITE CLIENT DOES NOT LIKE
http://www.tidemarque.com/
http://www.parlour-labels.com/
http://www.yonderpours.co.uk/aboutUs.html
http://www.graincorkhouse.com/
http://www.orbitmarques.co.uk/default.asp
http://www.summit-labels.co.uk/start.htm
http://www.durlay.co.uk/
http://www.pkcasks.com/default2.aspx
http://www.quaff-marques.co.uk/mainpage.aspx

COMPANY LOGO
Customer has a company logo (Supplied)

COLOURS:
Blue
White

STRAPLINE:
No

WEBSITE THEME: Marketing

IMAGES THAT BEST REFLECT THE COMPANY:
Spirits / Drinks

HEADER IMAGE:
Spirits / Brands

PAGES:
home
strength& flavour
a little about us
our spirit marketing
big brand success
speak to us

USER JOURNEYS:
General Service > Land on website >Navigation > Info Pages > Contact Form
Questions > Land on website > Message Banners > Info Pages > Contact Form
Contact > Land on website > Clear Telephone / Email Banner > Contact Form

CALL TO ACTION BANNER:
If you need help making your drink the next big brand, speak to us today.

KEYWORDS THAT RELATE TO THE BUSINESS:
brand marketing
drinks marketing
spirits marketing
brand marketing strategy
alcoholic drinks marketing
Drinks Brand Development

LOCATION(S):
United Kingdom -
Worldwide -

Target Market(s)

Male & Female
30-60
Marketing Directors
Brand Developers
Export Directors
Brand Managers

Industry/Entity Type

Marketing

Number of Pages Required

2 pages

Requirements
Must have
• This design will be integrated into wordpress, I have attached a wireframe of what we need, this is NOT a strict guide but contains content that is essential, the wireframes shows the priority of statements and products. the images supplied need to sell the products and services.
The main banner will eventually be animated so this needs to be taken into account.
The cliemt has supplied images which will need to be used in the design , however if you feel you have better images in the same style then they can be used.
Nice to have
• animation included, Jquery
Should not have
• NO fully flash sites or designs, this site will be Search engine optimised and updateable

```html
<!DOCTYPE html>
<html lang="en">
<head>
<meta charset="utf-8">
<title>Proof &amp; Palate — Drinks Brand Marketing</title>
<link rel="stylesheet" href="https://fonts.googleapis.com/css2?family=Arimo:wght@400;700&family=Patrick+Hand&display=swap">
<style>
:root{
  --blue:#0fa3dc;
  --blue-bright:#19b4ea;
  --ink:#0d2f3d;
  --text:#555;
  --muted:#6b6b6b;
  --line:#cfcfcf;
  --header-top:#ffffff;
  --header-bottom:#e9e9e9;
  --nav-top:#fafafa;
  --nav-bottom:#d6d6d6;
  --banner-deep:#021a24;
  --banner-mid:#083446;
  --glow:#dfe9ee;
  --pin:#c4c4c4;
  --hand:#6a6a6a;
}
*{box-sizing:border-box;margin:0;padding:0}
html,body{width:1200px;height:1020px;overflow:hidden;background:#fff}
body{font-family:"Arimo",Arial,sans-serif;color:var(--text);position:relative}

.site-header{height:193px;background:radial-gradient(ellipse at 40% 0%,var(--header-top) 0%,#f4f4f4 45%,var(--header-bottom) 100%);position:relative;border-bottom:2px solid #fff}
.brand{position:absolute;left:0;right:0;top:40px;display:flex;justify-content:center;align-items:center;gap:10px}
.brand-dot{width:14px;height:14px;border-radius:50%;background:var(--blue)}
.brand-name{font-size:22px;font-weight:700;color:#111;letter-spacing:.5px;text-transform:uppercase}
.contact{position:absolute;left:865px;top:133px;font-size:12px;color:var(--muted);line-height:15px}
.contact b{color:#555}
.contact a{color:var(--muted);text-decoration:none;border-bottom:1px solid #888}
.follow{display:flex;align-items:center;gap:6px;margin-top:5px;font-weight:700}
.social{width:16px;height:16px;border-radius:2px;display:inline-block}
.social.one{background:#3b5b98}
.social.two{background:#36b5e6;margin-left:4px}

.main-nav{height:58px;background:linear-gradient(var(--nav-top),#ececec 45%,var(--nav-bottom));position:relative;border-bottom:1px solid #bbb}
.main-nav ul{list-style:none;display:flex;position:absolute;left:131px;top:0;height:58px}
.main-nav li{display:flex;align-items:center;padding:0 23px;font-size:16px;color:#5a5a5a;text-shadow:0 1px 0 #fff;border-left:1px solid #c8c8c8;box-shadow:inset 1px 0 0 #f7f7f7}
.main-nav li:nth-child(2){border-left:none}
.main-nav li.current{background:var(--blue);color:#fff;font-weight:700;font-size:17px;text-shadow:none;border:none;position:relative;padding:0 24px}
.main-nav li.current::after{content:"";position:absolute;left:50%;bottom:-9px;margin-left:-9px;border:9px solid transparent;border-bottom:0;border-top-color:var(--blue)}

.hero{height:417px;position:relative;background:radial-gradient(ellipse 330px 300px at 370px 190px,var(--glow) 0%,#7f98a3 25%,var(--banner-mid) 60%,var(--banner-deep) 100%);overflow:hidden;border-bottom:2px solid #e5e5e5}
.hero-photo{position:absolute;left:250px;top:25px;width:240px;height:370px;border-radius:40px;background:radial-gradient(ellipse at 50% 30%,rgba(255,255,255,.55),rgba(190,205,210,.15) 60%,transparent 75%)}
.hero-quote{position:absolute;left:588px;top:95px;width:400px;font-size:39px;font-weight:700;line-height:50px;color:var(--blue-bright);text-shadow:0 2px 3px rgba(0,0,0,.6)}
.hero-cite{position:absolute;right:240px;top:250px;text-align:right;font-family:"Patrick Hand",cursive;font-size:31px;line-height:34px;color:var(--hand);text-shadow:0 1px 1px rgba(0,0,0,.6)}
.hero-arrow{position:absolute;top:185px}
.hero-arrow.prev{left:130px}
.hero-arrow.next{left:1036px}

.features{position:absolute;left:131px;top:700px;width:938px;display:flex;justify-content:space-between}
.feature{width:282px;position:relative;padding-left:38px}
.feature-pin{position:absolute;left:0;top:4px;width:26px;height:26px;border-radius:50%;background:var(--pin)}
.feature h2{font-weight:400;font-size:25px;line-height:31px;color:var(--ink)}
.feature p{font-size:12.5px;line-height:18px;color:var(--muted);margin:12px 0 0 4px}
.read-more{display:block;text-align:right;margin-top:22px;font-size:12.5px;font-weight:700;color:var(--blue);text-decoration:none}
.read-more span{border-bottom:1px solid var(--blue)}
.read-more::after{content:"";display:inline-block;margin-left:6px;border:5px solid transparent;border-right:0;border-left:6px solid var(--blue)}

.site-footer{position:absolute;left:131px;top:906px;width:938px;border-top:1px solid var(--line);text-align:center}
.keywords{margin-top:19px;font-size:12.5px;font-weight:700;color:#666}
.legal{margin-top:14px;font-size:11px;color:#666}
</style>
</head>
<body>
<header class="site-header">
  <div class="brand"><span class="brand-dot"></span><span class="brand-name">Proof &amp; Palate</span></div>
  <div class="contact">
    <div><b>T:</b> 020 7946 0321</div>
    <div><b>E:</b> <a href="#">info@proofandpalate.com</a></div>
    <div class="follow">Follow us: <span class="social one"></span><span class="social two"></span></div>
  </div>
</header>

<nav class="main-nav">
  <ul>
    <li class="current">home</li>
    <li>proof &amp; palate</li>
    <li>a little about us</li>
    <li>our spirit marketing</li>
    <li>big brand success</li>
    <li>speak to us</li>
  </ul>
</nav>

<section class="hero">
  <div class="hero-photo" role="img" aria-label="Martini glass with olives on a cocktail stick, lit against soft bokeh lights"></div>
  <svg class="hero-arrow prev" width="34" height="50" viewBox="0 0 34 50"><path d="M30 2 L6 25 L30 48 L22 48 L0 25 L22 2 Z" fill="#9a9a9a"/></svg>
  <blockquote class="hero-quote">“turning our small time whisky into a national brand”</blockquote>
  <div class="hero-cite">Daniel Hale<br>Vostrel</div>
  <svg class="hero-arrow next" width="34" height="50" viewBox="0 0 34 50"><path d="M4 2 L28 25 L4 48 L12 48 L34 25 L12 2 Z" fill="#9a9a9a"/></svg>
</section>

<main class="features">
  <article class="feature">
    <span class="feature-pin"></span>
    <h2>22 years experience with big brands</h2>
    <p>Lorem ipsum dolor sit amet, consectetur adipiscing elit. Aliquam id nisi nisi. Sed non erat nisi. Nam tincidunt diam ultrices tellus hendrerit vehicula vel sit amet.</p>
    <a class="read-more" href="#"><span>READ MORE</span></a>
  </article>
  <article class="feature">
    <span class="feature-pin"></span>
    <h2>Marketing your drink the next big brand</h2>
    <p>Lorem ipsum dolor sit amet, consectetur adipiscing elit. Aliquam id nisi nisi. Sed non erat nisi. Nam tincidunt diam ultrices tellus hendrerit vehicula vel sit amet.</p>
    <a class="read-more" href="#"><span>READ MORE</span></a>
  </article>
  <article class="feature">
    <span class="feature-pin"></span>
    <h2>350 outlets that listen to what we say</h2>
    <p>Lorem ipsum dolor sit amet, consectetur adipiscing elit. Aliquam id nisi nisi. Sed non erat nisi. Nam tincidunt diam ultrices tellus hendrerit vehicula vel sit amet.</p>
    <a class="read-more" href="#"><span>READ MORE</span></a>
  </article>
</main>

<footer class="site-footer">
  <p class="keywords">Brand Marketing &nbsp;|&nbsp; Brand Marketing Strategy &nbsp;|&nbsp; Drinks Marketing &nbsp;|&nbsp; Spirits Marketing &nbsp;|&nbsp; Alcohol Drinks Marketing &nbsp;|&nbsp; Drinks Brand Development</p>
  <p class="legal">© 1999 - 2010 Proof &amp; Palate | Terms &amp; Conditions | Privacy Policy</p>
</footer>
</body>
</html>
```